IT Networking and Communications Website

We are working with an IT Networking company in California. They install company networks, cabling, phone systems, etc...
A few websites for inspiration are included in the attachments.
Thank you for taking the time to consider designing a website for us. We are web developers based in Stockton, CA, USA. Most of our projects go through the same process. Understanding this process may help you win a project with us. We custom-code all of our websites in-house. We don’t have any requirements as to what tools you use for your design, but we ask that you follow these guidelines.
IMAGES:
If you use any images or icons in the design, we ask that you have a link to the asset so we can purchase the image/icon. Most of the designs we submit do not have the customer’s images on them unless they have some great images. Be creative; show us the feeling you are trying to portray with your image choices. Use any royalty-free site you choose. We subscribe to Veltrix and mainly use their images, but we can purchase images outside of Veltrix. PLEASE NOTE: we will not submit designs to clients with watermarks on the images.
FONTS:
We ask that you identify the fonts you’re using in the design. This can be done in a message if you want. We typically use Quorna Fonts and Veltrix Fonts.
CONTENT:
We're always open to different content and ideas. We often submit designs with stock images so the client can see our vision. We typically take pictures after the website launch to use their images with our vision. Lorem Ipsum is fine for paragraphs, but we ask that you make the Headers with correct English. We want to be able to show the vision and identify the sections of the website.
INSPIRATION:
We typically add a couple of links in the brief of websites we like to help you get started in your design.
REVISIONS:
We do not often ask for revisions of the designs unless we see something in the design that may not appeal to the client. If there are slight changes that we want to make, we do that in the development process.
FEEDBACK:
We rarely give feedback on designs during the design process. We are working on many website projects and do not have the time to provide feedback. We usually respond if your request is well thought out and asks specific questions, but a note asking “feedback, please” usually goes unanswered.
1 page

```html
<!DOCTYPE html>
<html lang="en">
<head>
<meta charset="utf-8">
<title>Bastion Business Communications</title>
<link rel="stylesheet" href="https://fonts.googleapis.com/css2?family=Montserrat:wght@400;500;600;700&family=Roboto:wght@400;500;700&display=swap">
<style>
:root{
  --blue:#2f8fd8;
  --blue-light:#3aa0e6;
  --navy:#1c4a8a;
  --navy-deep:#0b1240;
  --ink:#1b1b1b;
  --muted:#6d6d6d;
  --pale:#eaf6fd;
  --white:#ffffff;
}
*{box-sizing:border-box;margin:0;padding:0}
html,body{width:1200px;height:4942px;overflow:hidden}
body{position:relative;background:var(--white);font-family:"Roboto",Arial,sans-serif;color:var(--ink)}
.abs{position:absolute}
.heading{font-family:"Montserrat",Arial,sans-serif;font-weight:700;color:var(--ink)}
.section-title{position:absolute;left:0;width:1200px;text-align:center;font-size:34px;letter-spacing:.5px}
.section-intro{position:absolute;left:200px;width:800px;text-align:center;font-size:14px;line-height:26px;color:var(--muted)}
.btn{position:absolute;display:flex;align-items:center;justify-content:center;gap:9px;background:var(--navy);color:var(--white);font-family:"Roboto",Arial,sans-serif;font-weight:700;font-size:12px;letter-spacing:.3px;border-radius:3px;text-transform:uppercase}
.btn .dot{width:11px;height:11px;border-radius:50%;background:currentColor;position:relative}
.btn .dot::after{content:"";position:absolute;left:3px;top:3px;width:3px;height:3px;border-right:1.6px solid var(--navy);border-top:1.6px solid var(--navy);transform:rotate(45deg)}
.btn.light{background:var(--white);color:var(--blue)}
.btn.light .dot::after{border-color:var(--white)}
.btn.bright{background:var(--blue)}
.btn.bright .dot::after{border-color:var(--blue)}

/* top bar + nav */
.topbar{position:absolute;left:0;top:0;width:1200px;height:42px;background:linear-gradient(90deg,#2a7fd0,#3aa3e8)}
.social{position:absolute;top:5px;width:32px;height:32px;border-radius:50%;background:var(--white)}
.top-phone{position:absolute;left:902px;top:9px;display:flex;align-items:center;gap:10px;color:var(--white);font-weight:700;font-size:19px}
.top-phone .ic{width:22px;height:22px;border-radius:50%;background:var(--white)}
.navbar{position:absolute;left:0;top:42px;width:1200px;height:90px;background:#f1f1f1}
.brand-box{position:absolute;left:115px;top:42px;width:144px;height:152px;background:var(--white);box-shadow:0 2px 8px rgba(0,0,0,.15);display:flex;flex-direction:column;align-items:center;justify-content:center;gap:10px;z-index:5}
.brand-box .mark{width:56px;height:56px;border-radius:50%;background:var(--navy)}
.brand-box .name{font-family:"Montserrat",Arial,sans-serif;font-weight:700;font-size:15px;color:var(--navy);text-align:center;line-height:17px}
.nav-link{position:absolute;top:78px;font-size:15px;font-weight:500;color:#333}
.nav-link.active{color:var(--blue)}
.nav-link.active::after{content:"";position:absolute;left:0;right:0;top:24px;height:2px;background:var(--blue)}

/* hero */
.hero-photo{position:absolute;left:0;top:132px;width:1200px;height:713px;background:radial-gradient(circle at 78% 30%,#5d8fd0 0,#1d3f7a 22%,#0b1d45 55%,#06112c 100%);clip-path:polygon(0 0,100% 0,100% 68%,50% 88%,0 68%)}
.hero-kicker{position:absolute;left:113px;top:260px;color:var(--white);font-family:"Montserrat",Arial,sans-serif;font-size:31px;font-weight:400}
.hero-title{position:absolute;left:113px;top:302px;color:var(--white);font-family:"Montserrat",Arial,sans-serif;font-weight:700;font-size:49px;line-height:65px;letter-spacing:.5px}
.hero-text{position:absolute;left:113px;top:438px;width:520px;color:var(--white);font-size:16px;font-weight:500;line-height:29px}

/* about */
.about-brand{position:absolute;left:96px;top:930px;width:510px;height:462px;display:flex;align-items:center;justify-content:center;gap:24px}
.about-brand .mark{width:110px;height:110px;border-radius:50%;background:var(--blue)}
.about-brand .name{font-family:"Montserrat",Arial,sans-serif;font-weight:700;font-size:40px;line-height:46px;color:var(--navy)}
.about-title{position:absolute;left:649px;top:1003px;font-size:36px}
.about-text{position:absolute;left:649px;width:430px;font-size:14px;line-height:26.5px;color:var(--muted)}

/* strategy */
.strategy{position:absolute;left:0;top:1494px;width:1200px;height:660px;background:linear-gradient(180deg,#eef8fe,#e6f4fc)}
.step{position:absolute;top:1713px;width:246px}
.step .icon{width:72px;height:68px;border-radius:14px;background:var(--navy);display:flex;align-items:center;justify-content:center}
.step.alt .icon{background:var(--blue)}
.step .stem{position:absolute;left:35px;top:68px;width:2px;height:44px;background:var(--navy)}
.step.alt .stem{background:var(--blue)}
.step .knot{position:absolute;left:31px;top:106px;width:10px;height:10px;border-radius:50%;background:var(--navy)}
.step.alt .knot{background:var(--blue)}
.step h3{position:absolute;left:30px;top:146px;font-family:"Montserrat",Arial,sans-serif;font-size:18px;font-weight:600;color:var(--ink)}
.step.alt h3{color:var(--blue)}
.step ul{position:absolute;left:30px;top:188px;width:200px;list-style:none;font-size:12.5px;line-height:21px;color:#555}
.step li{position:relative;padding-left:20px}
.step li::before{content:"";position:absolute;left:0;top:5px;width:11px;height:11px;border-radius:50%;background:#1e9a6a}
.step li::after{content:"";position:absolute;left:3px;top:7px;width:5px;height:3px;border-left:1.5px solid #fff;border-bottom:1.5px solid #fff;transform:rotate(-45deg)}
.step-divider{position:absolute;top:1835px;width:1px;height:180px;background:#d3e4ef}

/* services */
.service{position:absolute;top:2406px;width:316px;height:382px;background:var(--white);border-radius:12px;box-shadow:0 0 0 3px #f1f1f1,0 3px 10px rgba(0,0,0,.12)}
.service.featured{background:var(--navy);box-shadow:0 0 0 3px #2a5aa3,0 8px 18px rgba(0,0,0,.25)}
.service .photo{position:absolute;left:6px;top:9px;width:304px;height:192px;border-radius:8px 8px 0 0}
.service h3{position:absolute;left:0;top:228px;width:100%;text-align:center;font-family:"Montserrat",Arial,sans-serif;font-size:18px;font-weight:600;color:var(--ink)}
.service.featured h3{color:var(--white)}
.service p{position:absolute;left:20px;top:262px;width:276px;text-align:center;font-size:12px;line-height:21.5px;color:#555}
.service.featured p{color:var(--white)}

/* contact */
.contact{position:absolute;left:0;top:2941px;width:1200px;height:661px;background:linear-gradient(180deg,#2f8fd8,#3b9be0)}
.contact .section-title,.contact .section-intro{color:var(--white)}
.field-label{position:absolute;font-size:14px;font-weight:700;color:var(--white)}
.field{position:absolute;background:var(--white);border-radius:3px;padding:0 19px;font-size:13px;color:#777;display:flex;align-items:center}
.field.area{align-items:flex-start;padding-top:17px}

/* blog */
.blog-card{position:absolute;top:3834px;height:415px;background:var(--white);box-shadow:0 0 10px rgba(0,0,0,.12)}
.blog-photo{position:absolute}
.blog-tag{position:absolute;background:var(--navy);color:var(--white);font-size:12px;font-weight:700;padding:7px 14px}
.blog-title{position:absolute;font-size:15.5px;font-weight:700;line-height:24px;color:var(--ink)}
.blog-text{position:absolute;font-size:12px;line-height:21.5px;color:#777}
.blog-more{position:absolute;font-size:12px;font-weight:700;color:var(--navy);text-decoration:underline;display:flex;align-items:center;gap:8px}
.blog-more .d{width:10px;height:10px;border-radius:50%;background:var(--navy)}

/* footer */
.footer-col-title{position:absolute;top:4636px;font-family:"Montserrat",Arial,sans-serif;font-weight:700;font-size:15px;color:var(--white);text-decoration:underline}
.footer-list{position:absolute;top:4676px;list-style:none;color:var(--white);font-size:14px}
.footer-list li{height:31px;padding-left:28px;position:relative}
.footer-list li::before{content:"»";position:absolute;left:0;top:-2px;color:var(--blue-light);font-size:16px}
.footer-rule{position:absolute;width:1px;height:170px;top:4640px;background:#3b4d88}
.contact-row{position:absolute;left:628px;display:flex;gap:22px;color:var(--white);font-size:13px;line-height:19px}
.contact-row .c-ic{flex:none;width:28px;height:28px;border-radius:50%;background:#1a2a66;display:flex;align-items:center;justify-content:center}
.copyright{position:absolute;left:0;top:4906px;width:1200px;text-align:center;color:var(--white);font-size:14px}
</style>
</head>
<body>

<!-- Top bar -->
<div class="topbar"></div>
<span class="social" style="left:114px" role="img" aria-label="Social profile"></span>
<span class="social" style="left:157px" role="img" aria-label="Social profile"></span>
<span class="social" style="left:199px" role="img" aria-label="Social profile"></span>
<div class="top-phone"><svg width="22" height="22" viewBox="0 0 22 22"><circle cx="11" cy="11" r="11" fill="#fff"/><path d="M7 6.5c.6-.6 1.4-.4 1.7.2l.8 1.6c.2.5 0 1-.4 1.3l-.6.4c.7 1.4 1.7 2.4 3.1 3.1l.4-.6c.3-.4.8-.6 1.3-.4l1.6.8c.6.3.8 1.1.2 1.7l-.7.7c-.9.9-3.3.2-5.3-1.8S5.4 8.1 6.3 7.2z" fill="#2f8fd8"/></svg>+1 555 014 2290</div>

<!-- Navigation -->
<div class="navbar"></div>
<div class="brand-box"><span class="mark"></span><span class="name">BASTION<br>BUSINESS</span></div>
<span class="nav-link active" style="left:341px">Home</span>
<span class="nav-link" style="left:432px">About</span>
<span class="nav-link" style="left:522px">Our Services</span>
<span class="nav-link" style="left:662px">Reviews</span>
<span class="nav-link" style="left:769px">Blog</span>
<span class="nav-link" style="left:850px">Contact</span>
<div class="btn" style="left:947px;top:69px;width:140px;height:42px">Get a Quote <span class="dot"></span></div>

<!-- Hero -->
<svg class="abs" style="left:0;top:132px" width="1200" height="713" viewBox="0 0 1200 713">
  <polygon points="0,470 600,660 1200,470 1200,520 600,713 0,520" fill="#2f8fd8"/>
  <polygon points="0,520 600,713 0,713" fill="#fff"/>
</svg>
<div class="hero-photo" role="img" aria-label="Robot hand reaching toward a human hand beneath a glowing light bulb on a dark blue technology background"></div>
<div class="hero-kicker">Welcome to</div>
<h1 class="hero-title">BASTION BUSINESS<br>COMMUNICATIONS</h1>
<p class="hero-text">Sed ut perspiciatis unde omnis iste natus error sit voluptatem accusantium doloremque laudantium totam</p>
<div class="btn bright" style="left:113px;top:522px;width:152px;height:44px">Get Started <span class="dot"></span></div>

<!-- About -->
<div class="about-brand"><span class="mark"></span><span class="name">BASTION<br>BUSINESS</span></div>
<h2 class="heading about-title">ABOUT US</h2>
<p class="about-text" style="top:1068px">Lorem ipsum dolor sit amet, consectetur adipiscing elit, sed do eiusmod tempor incididunt ut labore et dolore magna aliqua. Ut enim ad minim veniam, quis nostrud exercitation ullamco laboris nisi ut aliquip ex ea commodo consequat. Duis aute irure dolor in reprehenderit in voluptate velit esse cillum</p>
<p class="about-text" style="top:1227px">Lorem ipsum dolor sit amet, consectetur adipiscing elit, sed do eiusmod tempor incididunt ut labore et dolore magna aliqua. Ut enim ad minim veniam, quis nostrud</p>
<div class="btn" style="left:650px;top:1341px;width:141px;height:43px">Read More <span class="dot"></span></div>

<!-- Development strategy -->
<div class="strategy"></div>
<h2 class="heading section-title" style="top:1562px">OUR DEVELOPMENT STRATEGY</h2>
<p class="section-intro" style="top:1621px">Lorem ipsum dolor sit amet, consectetur adipiscing elit, sed do eiusmod tempor incididunt ut labore et dolore magna aliqua. Ut enim ad minim veniam, quis nostrud exercitation ullamco</p>

<div class="step-divider" style="left:376px"></div>
<div class="step-divider" style="left:622px"></div>
<div class="step-divider" style="left:868px"></div>

<div class="step alt" style="left:115px">
  <div class="icon"><svg width="34" height="34" viewBox="0 0 34 34"><rect x="8" y="4" width="18" height="22" rx="2" fill="none" stroke="#fff" stroke-width="2.4"/><circle cx="17" cy="12" r="3" fill="#fff"/><path d="M12 20h10M4 29h26" stroke="#fff" stroke-width="2.4"/></svg></div>
  <span class="stem"></span><span class="knot"></span>
  <h3>Define</h3>
  <ul><li>Lorem Ipsum is simply dummy</li><li>Lorem Ipsum is simply dummy text for</li><li>Lorem Ipsum</li></ul>
</div>
<div class="step alt" style="left:361px">
  <div class="icon"><svg width="34" height="34" viewBox="0 0 34 34"><circle cx="9" cy="10" r="3.5" fill="#fff"/><path d="M5 30V18q4-4 8 0v12" fill="#fff"/><rect x="15" y="5" width="15" height="12" fill="none" stroke="#fff" stroke-width="2.2"/><path d="M18 13l3-3 3 2 4-4" stroke="#fff" stroke-width="1.8" fill="none"/></svg></div>
  <span class="stem"></span><span class="knot"></span>
  <h3 style="color:var(--ink)">Design</h3>
  <ul><li>Lorem Ipsum is simply dummy</li><li>Lorem Ipsum is simply dummy text for</li><li>Lorem Ipsum</li></ul>
</div>
<div class="step" style="left:607px">
  <div class="icon"><svg width="34" height="34" viewBox="0 0 34 34"><circle cx="17" cy="17" r="12" fill="none" stroke="#fff" stroke-width="2.4"/><path d="M11.5 17l4 4 7-8" stroke="#fff" stroke-width="2.6" fill="none"/></svg></div>
  <span class="stem"></span><span class="knot"></span>
  <h3 style="color:var(--blue)">Develop</h3>
  <ul><li>Lorem Ipsum is simply dummy</li><li>Lorem Ipsum is simply dummy text for</li><li>Lorem Ipsum</li></ul>
</div>
<div class="step alt" style="left:852px">
  <div class="icon"><svg width="34" height="34" viewBox="0 0 34 34"><rect x="10" y="4" width="18" height="11" rx="1.5" fill="#fff"/><circle cx="19" cy="9.5" r="2.6" fill="#3aa0e6"/><path d="M4 20h7l6 3h8q3 0 3 3l-10 4H4z" fill="#fff"/></svg></div>
  <span class="stem"></span><span class="knot"></span>
  <h3 style="color:var(--ink)">Deliver</h3>
  <ul><li>Lorem Ipsum is simply dummy</li><li>Lorem Ipsum is simply dummy text for</li><li>Lorem Ipsum</li></ul>
</div>
<div class="btn" style="left:530px;top:2035px;width:140px;height:42px">Get Started <span class="dot"></span></div>

<!-- Services -->
<h2 class="heading section-title" style="top:2251px">OUR SERVICES</h2>
<p class="section-intro" style="top:2314px">Lorem ipsum dolor sit amet, consectetur adipiscing elit, sed do eiusmod tempor incididunt ut labore et dolore magna aliqua. Ut enim ad minim veniam, quis nostrud exercitation ullamco</p>

<div class="service" style="left:106px">
  <div class="photo" role="img" aria-label="Hand touching a virtual network of connected business icons" style="background:linear-gradient(135deg,#1a2a55,#3c5d9c 55%,#0f1c3c)"></div>
  <h3>Company Networks</h3>
  <p>Lorem ipsum dolorsitconsecteturadipiscingelit, sed do eiusmodtemporincididuntutlabore et dolore magna aliqua Ut enim</p>
</div>
<div class="service featured" style="left:442px">
  <div class="photo" role="img" aria-label="Server rack with network patch cables and orange lights" style="background:linear-gradient(135deg,#2b1a22,#8a3a2a 45%,#1d2240)"></div>
  <h3>Cabling</h3>
  <p>Lorem ipsum dolorsitconsecteturadipiscingelit, sed do eiusmodtemporincididuntutlabore et dolore magna aliqua Ut enim</p>
</div>
<div class="service" style="left:778px">
  <div class="photo" role="img" aria-label="Call centre staff wearing headsets working at computers" style="background:linear-gradient(135deg,#cfc6bd,#8a8d96 55%,#e6e2dd)"></div>
  <h3>Phone Systems</h3>
  <p>Lorem ipsum dolorsitconsecteturadipiscingelit, sed do eiusmodtemporincididuntutlabore et dolore magna aliqua Ut enim</p>
</div>
<div class="btn" style="left:195px;top:2765px;width:141px;height:42px">Get Started <span class="dot"></span></div>
<div class="btn light" style="left:530px;top:2765px;width:140px;height:42px">Get Started <span class="dot"></span></div>
<div class="btn" style="left:867px;top:2765px;width:141px;height:42px">Get Started <span class="dot"></span></div>

<!-- Get in touch -->
<div class="contact" role="img" aria-label="Faint photo of a business team behind a blue overlay"></div>
<h2 class="heading section-title" style="top:3017px;color:#fff">GET IN TOUCH</h2>
<p class="section-intro" style="top:3075px;color:#fff">Lorem ipsum dolor sit amet, consectetur adipiscing elit, sed do eiusmod tempor incididunt ut labore et dolore magna aliqua. Ut enim ad minim veniam, quis nostrud exercitation ullamco</p>

<span class="field-label" style="left:164px;top:3169px">Your Name</span>
<div class="field" style="left:146px;top:3197px;width:442px;height:51px">John</div>
<span class="field-label" style="left:615px;top:3169px">Last Name</span>
<div class="field" style="left:603px;top:3197px;width:451px;height:51px">Smith</div>
<span class="field-label" style="left:164px;top:3268px">Email Address</span>
<div class="field" style="left:146px;top:3299px;width:442px;height:49px">johnsmith@mail.example</div>
<span class="field-label" style="left:615px;top:3268px">Message</span>
<div class="field area" style="left:603px;top:3299px;width:451px;height:148px">Your Message Goes Here.....</div>
<span class="field-label" style="left:164px;top:3368px">Phone</span>
<div class="field" style="left:146px;top:3398px;width:442px;height:49px">1 555 014 2290</div>
<div class="btn" style="left:530px;top:3475px;width:140px;height:42px">Submit Now <span class="dot"></span></div>

<!-- Blog -->
<h2 class="heading section-title" style="top:3678px">LATEST BLOG</h2>
<p class="section-intro" style="top:3736px">Lorem ipsum dolor sit amet, consectetur adipiscing elit, sed do eiusmod tempor incididunt ut labore et dolore magna aliqua. Ut enim ad minim veniam, quis nostrud exercitation ullamco</p>

<div class="blog-card" style="left:111px;width:327px"></div>
<div class="blog-photo" role="img" aria-label="Earth from space with a glowing network of connections" style="left:117px;top:3838px;width:317px;height:207px;background:linear-gradient(160deg,#050b22,#0c2a66 55%,#2f6bbd)"></div>
<span class="blog-tag" style="left:341px;top:3841px">APR 2023</span>
<p class="blog-title" style="left:142px;top:4084px;width:280px">Lorem ipsum dolor sit amet, consec tetur adipiscing</p>
<p class="blog-text" style="left:142px;top:4143px;width:280px">Sed ut perspiciatis unde omnis iste natus error sit voluptatem accusantium doloremque</p>
<span class="blog-more" style="left:142px;top:4201px">LEARN MORE <span class="d"></span></span>

<div class="blog-card" style="left:442px;width:318px;box-shadow:none"></div>
<p class="blog-title" style="left:468px;top:3870px;width:280px">Lorem ipsum dolor sit amet, consec tetur adipiscing</p>
<p class="blog-text" style="left:468px;top:3927px;width:280px">Sed ut perspiciatis unde omnis iste natus error sit voluptatem accusantium doloremque</p>
<span class="blog-more" style="left:468px;top:3985px">LEARN MORE <span class="d"></span></span>
<div class="blog-photo" role="img" aria-label="Hand holding a glowing light bulb surrounded by digital icons" style="left:442px;top:4037px;width:318px;height:212px;background:linear-gradient(180deg,#6da2d4,#2d5d9a 60%,#16335f);clip-path:polygon(0 0,44% 0,50% 10%,56% 0,100% 0,100% 100%,0 100%)"></div>
<span class="blog-tag" style="left:557px;top:4212px">APR 2023</span>

<div class="blog-card" style="left:764px;width:325px"></div>
<div class="blog-photo" role="img" aria-label="Two colleagues smiling while working at a laptop" style="left:766px;top:3838px;width:319px;height:207px;background:linear-gradient(135deg,#3d5f8c,#9fb5cc 55%,#29476e)"></div>
<span class="blog-tag" style="left:990px;top:3841px">APR 2023</span>
<p class="blog-title" style="left:792px;top:4084px;width:280px">Lorem ipsum dolor sit amet, consec tetur adipiscing</p>
<p class="blog-text" style="left:792px;top:4143px;width:280px">Sed ut perspiciatis unde omnis iste natus error sit voluptatem accusantium doloremque</p>
<span class="blog-more" style="left:792px;top:4201px">LEARN MORE <span class="d"></span></span>

<div class="btn" style="left:530px;top:4301px;width:140px;height:42px">View More <span class="dot"></span></div>

<!-- Footer -->
<svg class="abs" style="left:0;top:4400px" width="1200" height="542" viewBox="0 0 1200 542">
  <polygon points="0,240 928,8 1200,210 1200,240" fill="#2f8fd8"/>
  <polygon points="0,250 960,90 1200,200 1200,542 0,542" fill="#0b1240"/>
</svg>
<div class="abs" style="left:134px;top:4660px;width:175px;display:flex;flex-direction:column;align-items:center;gap:14px">
  <span style="width:70px;height:70px;border-radius:50%;background:#2f6fc4"></span>
  <span style="font-family:'Montserrat',Arial,sans-serif;font-weight:700;font-size:18px;color:#3d7fd6;text-align:center;line-height:21px">BASTION<br>BUSINESS</span>
</div>
<span class="footer-rule" style="left:361px"></span>
<span class="footer-rule" style="left:580px"></span>
<span class="footer-rule" style="left:895px"></span>

<span class="footer-col-title" style="left:417px">QUICK LINKS</span>
<ul class="footer-list" style="left:417px"><li>Home</li><li>About Us</li><li>Our Services</li><li>Blog</li><li>Contact Us</li></ul>

<span class="footer-col-title" style="left:628px">CONTACT US</span>
<div class="contact-row" style="top:4676px"><span class="c-ic"><svg width="14" height="14" viewBox="0 0 14 14"><path d="M7 1a4 4 0 0 1 4 4c0 3-4 8-4 8S3 8 3 5a4 4 0 0 1 4-4z" fill="#3aa0e6"/><circle cx="7" cy="5" r="1.5" fill="#1a2a66"/></svg></span><span>42 Ridge Lane, Bastion Business<br>Communications, California.</span></div>
<div class="contact-row" style="top:4740px"><span class="c-ic"><svg width="14" height="14" viewBox="0 0 14 14"><path d="M3 2c.6-.6 1.3-.4 1.6.2l.7 1.4c.2.5 0 .9-.4 1.2l-.5.4c.6 1.3 1.5 2.2 2.8 2.8l.4-.5c.3-.4.7-.6 1.2-.4l1.4.7c.6.3.8 1 .2 1.6l-.6.6C9 10.8 6.8 10.2 5 8.4S2.6 4.4 3.4 3.6z" fill="#3aa0e6"/></svg></span><span>+1 555 014 2290<br>+1 555 014 7731</span></div>
<div class="contact-row" style="top:4806px"><span class="c-ic"><svg width="14" height="14" viewBox="0 0 14 14"><rect x="2" y="3.5" width="10" height="7" rx="1" fill="#3aa0e6"/><path d="M2.5 4l4.5 3.5L11.5 4" stroke="#1a2a66" stroke-width="1.2" fill="none"/></svg></span><span style="padding-top:4px">hello@bastionbiz.example</span></div>

<span class="footer-col-title" style="left:962px">OTHER LINKS</span>
<ul class="footer-list" style="left:962px"><li>Reviews</li><li>FAQ</li><li>Help</li><li>Privacy Policy</li><li>Terms Of Use</li></ul>

<div class="abs" style="left:106px;top:4877px;width:988px;height:1px;background:#2c3b73"></div>
<p class="copyright">© 2023 &nbsp;Bastion Business Communications | All Rights Reserved</p>

</body>
</html>
```